Business Cards for a Luggage Service (Repair, Sales, Warranty Etc.) Company
Belmora Baggage Services
Professional
Gregory Talvane
Owner
2418 Quillon Ave. Suite 320 Atlanta, GA 30987
Info@BelmoraBaggageServices.example
www.BelmoraBaggageServices.example
The logo was made for my sign. So it's a bit big.
tkalvin tkalvin
Our company is a luggage service company. We repair luggage, provide warranty related services, and sell new luggage. We are located within 1 mile of Atlanta's Pembrook Dallow International Airport (worlds busiest airport). We specialize in flight crew luggage repair and services.

```html
<!DOCTYPE html>
<html lang="en">
<head>
<meta charset="utf-8">
<title>Belmora Baggage Services – Business Cards</title>
<link href="https://fonts.googleapis.com/css2?family=Open+Sans:wght@400;600;700&display=swap" rel="stylesheet">
<style>
  :root {
    --bg: #e9e7e4;
    --card: #ffffff;
    --ink: #1a1a1a;
    --black: #111111;
    --red: #d42a2a;
    --grey: #6b6b6b;
    --line: #9a9a9a;
  }
  * { box-sizing: border-box; margin: 0; padding: 0; }
  html, body { width: 1200px; height: 782px; overflow: hidden; }
  body {
    background: var(--bg);
    font-family: "Open Sans", Arial, sans-serif;
    color: var(--ink);
    display: flex;
    align-items: center;
    justify-content: center;
    gap: 40px;
  }
  .card {
    position: relative;
    width: 560px;
    height: 320px;
    background: var(--card);
    border-radius: 22px;
    overflow: hidden;
    box-shadow: 0 6px 18px rgba(0,0,0,.18);
  }
  .card-swoosh { position: absolute; inset: 0; width: 100%; height: 100%; }
  .brand {
    position: absolute;
    display: flex;
    flex-direction: column;
    align-items: flex-start;
  }
  .brand-row { display: flex; align-items: center; gap: 10px; }
  .brand-mark { width: 34px; height: 34px; background: var(--red); }
  .brand-name {
    font-weight: 700;
    color: var(--ink);
    font-size: 21px;
    letter-spacing: .5px;
    text-transform: uppercase;
    line-height: 1.05;
  }
  .brand-tagline {
    margin-top: 6px;
    margin-left: 44px;
    display: flex;
    gap: 28px;
    font-size: 8px;
    letter-spacing: 1px;
    color: var(--grey);
  }
  .card--back .brand { left: 118px; top: 140px; }
  .card--front .brand { left: 34px; top: 148px; }
  .card--front .brand-name { font-size: 17px; }
  .divider {
    position: absolute;
    left: 296px;
    top: 140px;
    width: 1px;
    height: 140px;
    background: var(--line);
  }
  .holder {
    position: absolute;
    right: 26px;
    top: 40px;
    text-align: right;
    color: #fff;
  }
  .holder-name { font-size: 15px; font-weight: 600; }
  .holder-title { font-size: 13px; }
  .contact {
    position: absolute;
    left: 310px;
    top: 142px;
    list-style: none;
    font-size: 12px;
    line-height: 21px;
    color: var(--ink);
  }
  .contact li { display: flex; align-items: center; gap: 6px; }
  .contact svg { width: 11px; height: 11px; fill: var(--ink); flex: none; }
  .contact .address { display: block; line-height: 16px; margin-bottom: 4px; }
</style>
</head>
<body>

  <section class="card card--back" aria-label="Card back">
    <svg class="card-swoosh" viewBox="0 0 560 320" aria-hidden="true">
      <path d="M0,0 H560 V78 C400,22 200,8 0,34 Z" fill="var(--black)"/>
      <path d="M0,48 C200,20 400,36 560,96" fill="none" stroke="var(--red)" stroke-width="4"/>
    </svg>
    <div class="brand">
      <div class="brand-row">
        <span class="brand-mark"></span>
        <span class="brand-name">Belmora Baggage Services</span>
      </div>
      <div class="brand-tagline"><span>REPAIRS</span><span>WARRANTY</span><span>SALES</span></div>
    </div>
  </section>

  <section class="card card--front" aria-label="Card front">
    <svg class="card-swoosh" viewBox="0 0 560 320" aria-hidden="true">
      <path d="M160,0 H560 V118 C440,64 300,22 160,0 Z" fill="var(--black)"/>
      <path d="M40,8 C250,30 420,78 560,138" fill="none" stroke="var(--red)" stroke-width="4"/>
    </svg>
    <div class="holder">
      <p class="holder-name">Gregory Talvane</p>
      <p class="holder-title">Owner</p>
    </div>
    <div class="brand">
      <div class="brand-row">
        <span class="brand-mark"></span>
        <span class="brand-name">Belmora Baggage<br>Services</span>
      </div>
      <div class="brand-tagline"><span>REPAIRS</span><span>WARRANTY</span><span>SALES</span></div>
    </div>
    <span class="divider"></span>
    <ul class="contact">
      <li class="address">2418 Quillon Ave. Suite 320<br>Atlanta, GA 30987</li>
      <li><svg viewBox="0 0 24 24"><path d="M6.6 10.8a15 15 0 0 0 6.6 6.6l2.2-2.2c.3-.3.7-.4 1-.2 1.1.4 2.3.6 3.6.6.6 0 1 .4 1 1V20c0 .6-.4 1-1 1A17 17 0 0 1 3 4c0-.6.4-1 1-1h3.5c.6 0 1 .4 1 1 0 1.3.2 2.5.6 3.6.1.3 0 .7-.2 1z"/></svg>012 555 0147</li>
      <li><svg viewBox="0 0 24 24"><path d="M7 1h10a2 2 0 0 1 2 2v18a2 2 0 0 1-2 2H7a2 2 0 0 1-2-2V3a2 2 0 0 1 2-2zm0 3v14h10V4z"/></svg>012 555 0148</li>
      <li><svg viewBox="0 0 24 24"><path d="M2 5h20v14H2zm2 2v.5l8 5 8-5V7z"/></svg>Info@BelmoraBaggageServices.example</li>
      <li>www.BelmoraBaggageServices.example</li>
    </ul>
  </section>

</body>
</html>
```